Sumworks.co.uk - front page and content page design
Site design for Sumworks.co.uk - a UK site hosting different calculators
Creative Brief
Internet Services
http://www.plotmeadow.co.uk
Project: Sumworks.co.uk
Idea: To host all of the different types of calculators on the site with supporting content
Our idea is generating targeted traffic through generic domains (we've got 4,500!). With Sumworks.co.uk, the domain will host loads of different calculators with content supporting the calculators on offer.
For Sumworks.co.uk, we'd like a design that is clean but colourful and allows us to colour the different sections of the site that we'll have. The initial premise is that we'll have sections for the different 'types' of calculators:
Health calculators
Finance calculators
Maths calculators
Conversion calculators
Pregnancy calculators
Within each section will be different calculators - so, for example, in Health, there will be a BMI calculator, BMR calculator and so on.
Ideally, we'd like each 'section' to have a different colour - i.e. blue for Health, green for Finance, blue for Maths, etc. The colours can be chosen by the designer as to what looks best.
We'd like a front page design and also a content page design. The home page shouldn't be too different in structure/layout to the content pages (i.e. structure follows through).
Ideally, there will be a column on the right hand side that allows advertising (300 x 250) and the main column for content should be at least 540px (this is where content and weidgets/calculators will be placed).
Once in a section, there should be a left menu that allows users to choose the type of calculator they want within that section.
This is our first try on Pixelgrove and we're hoping that if this works out, we can find some designer(s) through this who we can offer many more design projects as we have many generic domain names waiting to be designed.
Likes: Clean, colourful, elegant, professional
www.vitalpage.com
http://www.brightjotapp.com/tour/why-use-brightjot
http://www.kelvo.com/

```html
<!DOCTYPE html>
<html lang="en">
<head>
<meta charset="utf-8">
<title>Sumworks.co.uk – Health Calculators</title>
<link rel="stylesheet" href="https://fonts.googleapis.com/css2?family=Gelasio:wght@400;700&family=Arimo:wght@400;700&display=swap">
<style>
:root{
  --health:#6cc51c; --health-dark:#4f9a0f;
  --finance:#5fa8e8; --maths:#ee5a5a; --conversion:#f59a2a; --pregnancy:#d46fd6;
  --accent:#f47c20;
  --ink:#333; --muted:#777; --line:#d8d8d8;
  --widget-top:#c6d3de; --widget-bottom:#98adbf; --widget-edge:#6f8699;
  --button-top:#b9dcf7; --button-bottom:#6fb2e6;
  --footer:#e6e6e6;
}
*{box-sizing:border-box;margin:0;padding:0}
html,body{width:1200px;height:917px;overflow:hidden}
body{position:relative;background:linear-gradient(#fff 0,#f1f1f1 760px,#fff 760px,#fff 836px,var(--footer) 836px);font-family:"Arimo",sans-serif;color:var(--ink)}
.abs{position:absolute}

/* header */
.brand{left:110px;top:58px;display:flex;align-items:center;gap:12px}
.brand-mark{width:34px;height:34px;background:var(--accent)}
.brand-name{font-family:"Arimo",sans-serif;font-size:40px;color:#7aab2c;font-weight:400;letter-spacing:-.5px}
.section-tabs{left:602px;top:30px;display:flex;gap:6px;list-style:none}
.section-tabs li{height:44px;padding:0 16px;line-height:44px;color:#fff;font-family:"Gelasio",serif;font-size:17px;border-radius:3px 3px 0 0;box-shadow:inset 0 -4px 0 rgba(0,0,0,.12)}
.tab-health{background:var(--health)}.tab-finance{background:var(--finance)}
.tab-maths{background:var(--maths)}.tab-conversion{background:var(--conversion)}
.tab-pregnancy{background:var(--pregnancy)}
.search{left:850px;top:108px;width:236px;height:22px;border:1px solid var(--line);border-radius:11px;background:#fff;font-size:11px;color:#999;line-height:20px;padding-left:10px}
.search-btn{position:absolute;right:-1px;top:-1px;width:36px;height:22px;border-radius:11px;background:var(--accent)}

/* main panel */
.panel{left:95px;top:160px;width:1010px;height:585px;background:#fff;border-radius:6px;box-shadow:0 0 14px rgba(0,0,0,.18)}
.side-nav{left:90px;top:180px;width:153px}
.side-active{height:33px;background:var(--health);color:#fff;font-family:"Gelasio",serif;font-size:20px;padding-left:26px;line-height:33px;border-radius:0 4px 4px 0}
.sub-list{list-style:none;margin:6px 0 0 24px}
.sub-list li{height:24px;margin-bottom:2px;border:1px solid var(--line);font-size:12px;line-height:22px;padding-left:4px;width:110px}
.sub-list .current{color:var(--accent)}
.section-list{list-style:none;margin:20px 0 0 24px;font-family:"Gelasio",serif;font-size:20px}
.section-list li{height:41px}

/* calculator */
.calc{left:240px;top:168px;width:542px;height:302px;border:3px solid var(--widget-edge);border-radius:4px;background:linear-gradient(var(--widget-top),var(--widget-bottom))}
.calc h2{position:absolute;left:14px;top:16px;font-family:"Gelasio",serif;font-size:21px;font-weight:400;color:#222}
.unit-bar{position:absolute;top:70px;height:28px;background:linear-gradient(#f4f4f4,#d6d6d6);border:1px solid #aab;font-family:"Gelasio",serif;font-size:16px;line-height:26px;padding-left:10px}
.or{position:absolute;left:342px;top:72px;font-family:"Gelasio",serif;font-size:16px}
.field-label{position:absolute;font-size:11px;font-weight:700;color:#223}
.input{position:absolute;height:18px;background:#fff;border:1px solid #8899aa}
.unit{position:absolute;font-size:11px;color:#223}
.btn{position:absolute;top:248px;height:29px;border-radius:4px;border:1px solid #4d86b5;background:linear-gradient(var(--button-top),var(--button-bottom));font-size:14px;color:#123;text-align:center;line-height:27px}

/* ads */
.ad{position:absolute}
.ad-main{left:789px;top:168px;width:298px;height:242px;background:linear-gradient(135deg,#3a3a3a,#cfd3d6 70%,#eee)}
.ad-a{left:797px;top:427px;width:138px;height:138px;background:linear-gradient(#2c5a8c,#e2b23b)}
.ad-b{left:943px;top:427px;width:141px;height:138px;background:linear-gradient(135deg,#1e2c5a,#c93a6a,#f2c03a)}
.ad-c{left:797px;top:575px;width:138px;height:139px;background:linear-gradient(#333,#6a4a2a)}
.ad-d{left:943px;top:575px;width:141px;height:139px;background:linear-gradient(#1a1a1a,#e85c1c,#3ab0e0)}

/* copy */
.content-title{left:272px;top:490px;font-family:"Gelasio",serif;font-size:26px;font-weight:400;color:var(--health)}
.copy{left:272px;top:530px;width:500px;font-size:12px;line-height:15.5px;color:#666}
.copy p{margin-bottom:13px}

/* bookmark bar */
.bookmarks{left:112px;top:788px;display:flex;align-items:center;gap:18px;font-size:10px;color:#5577aa}
.bookmarks .lead{color:#999}
.bookmarks span.item{display:flex;align-items:center;gap:4px}
.dot{width:9px;height:9px;background:#9ab}
.feed-badge{left:850px;top:788px;width:70px;height:14px;background:#e89a3a}
.feed{left:975px;top:785px;display:flex;gap:8px;align-items:center;font-size:11px;color:#555}
.feed .sq{width:16px;height:16px;background:var(--accent);border-radius:3px}

/* footer */
.footer-nav{left:112px;top:844px;font-size:11px;color:#555;word-spacing:3px}
.copyright{left:112px;top:862px;font-size:11px;color:#555}
.footer-brand{left:912px;top:838px;display:flex;align-items:center;gap:8px}
.footer-brand .sq{width:22px;height:22px;background:#b0b0b0}
.footer-brand span{font-size:26px;color:#a8a8a8}
</style>
</head>
<body>
<header>
  <div class="abs brand"><div class="brand-mark"></div><span class="brand-name">Sumworks.co.uk</span></div>
  <ul class="abs section-tabs">
    <li class="tab-health">Health</li><li class="tab-finance">Finance</li><li class="tab-maths">Maths</li><li class="tab-conversion">Conversion</li><li class="tab-pregnancy">Pregnancy</li>
  </ul>
  <div class="abs search">Search this site<span class="search-btn"></span></div>
</header>

<main>
  <div class="abs panel"></div>
  <nav class="abs side-nav">
    <div class="side-active">Health</div>
    <ul class="sub-list"><li>BMI Calculator</li><li class="current">BMR Calculator</li><li>Other Calculator</li></ul>
    <ul class="section-list"><li>Finance</li><li>Maths</li><li>Conversion</li><li>Pregnancy</li></ul>
  </nav>

  <section class="abs calc">
    <h2>BMR Calculator</h2>
    <div class="unit-bar" style="left:15px;width:284px">Standard</div>
    <div class="or">OR</div>
    <div class="unit-bar" style="left:332px;width:193px">Metric</div>

    <div class="field-label" style="left:27px;top:122px">Your Height:</div>
    <div class="input" style="left:27px;top:139px;width:68px"></div><div class="unit" style="left:103px;top:141px">Feet and</div>
    <div class="input" style="left:160px;top:139px;width:68px"></div><div class="unit" style="left:236px;top:141px">Inches</div>
    <div class="field-label" style="left:27px;top:190px">Your Weight:</div>
    <div class="input" style="left:27px;top:207px;width:68px"></div><div class="unit" style="left:103px;top:209px">Pounds</div>

    <div class="field-label" style="left:350px;top:122px">Your Height:</div>
    <div class="input" style="left:350px;top:139px;width:68px"></div><div class="unit" style="left:426px;top:141px">Centimeters</div>
    <div class="field-label" style="left:350px;top:190px">Your Weight:</div>
    <div class="input" style="left:350px;top:207px;width:68px"></div><div class="unit" style="left:426px;top:209px">Kilogram</div>

    <div class="btn" style="left:30px;width:128px">Calculate</div>
    <div class="btn" style="left:170px;width:98px">Reset</div>
    <div class="btn" style="left:341px;width:98px">Calculate</div>
    <div class="btn" style="left:447px;width:72px">Reset</div>
  </section>

  <aside>
    <div class="ad ad-main" role="img" aria-label="Car advertisement banner, 300 by 250"></div>
    <div class="ad ad-a" role="img" aria-label="Business cards software advertisement"></div>
    <div class="ad ad-b" role="img" aria-label="Vector graphics pack advertisement"></div>
    <div class="ad ad-c" role="img" aria-label="Mac software free demos advertisement"></div>
    <div class="ad ad-d" role="img" aria-label="Cartoon drawing training videos advertisement"></div>
  </aside>

  <h1 class="abs content-title">Health Calculator</h1>
  <div class="abs copy">
    <p>Lorem ipsum dolor sit amet, consectetur adipiscing elit. Suspendisse risus est, feugiat vel congue a, volutpat eget ipsum. Vestibulum quis ligula in risus tempus sagittis ac venenatis turpis. Aliquam ullamcorper tristique justo at cursus.</p>
    <p>Sed suscipit, velit vitae blandit aliquet, est lacus blandit quam, in adipiscing dui risus commodo lorem. Nullam lobortis scelerisque sem, euismod imperdiet turpis placerat sit amet.</p>
    <p>Cum sociis natoque penatibus et magnis dis parturient montes, nascetur ridiculus mus. Proin tempus massa sit amet lectus ultricies eget elementum tellus varius.</p>
  </div>
</main>

<div class="abs bookmarks">
  <span class="lead">bookmark with</span>
  <span class="item"><i class="dot"></i>Savorly</span><span class="item"><i class="dot"></i>Dugout</span>
  <span class="item"><i class="dot"></i>Searchly</span><span class="item"><i class="dot"></i>Friendbook</span>
  <span class="item"><i class="dot"></i>Wanderly</span><span class="item"><i class="dot"></i>Linkbay</span>
</div>
<div class="abs feed-badge"></div>
<div class="abs feed"><span class="sq"></span>Get Latest Feed</div>

<footer>
  <div class="abs footer-nav">Home &nbsp;|&nbsp; About Us &nbsp;|&nbsp; Services &nbsp;|&nbsp; Types of Calculator &nbsp;|&nbsp; Contact Us</div>
  <div class="abs copyright">Copyright © 2011, <b>Sumworks.co.uk</b>. All rights reserved.</div>
  <div class="abs footer-brand"><span class="sq"></span><span>Sumworks.co.uk</span></div>
</footer>
</body>
</html>
```